KBR, LLC Original

I need a business card design for a new company in Gaithersburg, MD. Though the name of the company is Wiring By Candor (KBR) we specialize in commercial kitchen ventilation systems as a complete turnkey project or as a service provider. We can design the entire system including the hoods, fans, ductwork, and fire system. We also specialize in fire alarm service, design, install and inspection. We are experts on any Pellmoor Units equipment including Vexa PCU, Vexa Hoods, EMS controls, Standard controls, PCU filtration and Make-up Air units with heaters and cooling. We can repair/retrofit old water wash hood systems as well. We are experts with local code requirements and upgrades.

Industry/Entity Type

Business

Contact Information for Business Card

Neil Radcott, Wiring By Candor, LLC; 240-555-0182 Cell, Fernbrooke, MD 20990. Neilr@wiringbycandorco.example

```html
<!DOCTYPE html>
<html lang="en">
<head>
<meta charset="utf-8">
<title>Wiring By Candor, LLC — Business Card</title>
<link rel="stylesheet" href="https://fonts.googleapis.com/css2?family=Lato:wght@400;700;900&display=swap">
<style>
  :root {
    --page-bg: #d9d9d9;
    --card-bg: #efefee;
    --ink: #141414;
    --card-shadow: rgba(0, 0, 0, 0.22);
  }
  * { margin: 0; padding: 0; box-sizing: border-box; }
  html, body {
    width: 1200px;
    height: 926px;
    overflow: hidden;
    background: var(--page-bg);
    font-family: "Lato", sans-serif;
    color: var(--ink);
  }
  .canvas {
    width: 1200px;
    height: 926px;
    display: flex;
    flex-direction: column;
    align-items: center;
    justify-content: center;
    gap: 48px;
  }
  .card {
    position: relative;
    width: 660px;
    height: 377px;
    background: var(--card-bg);
    box-shadow: 0 6px 18px var(--card-shadow);
  }
  .card-back {
    display: flex;
    align-items: center;
    justify-content: center;
  }
  .company-name {
    font-weight: 900;
    font-size: 38px;
    letter-spacing: 0.2px;
    margin-top: -20px;
  }
  .person-name {
    position: absolute;
    top: 110px;
    left: 0;
    right: 0;
    text-align: center;
    font-weight: 700;
    font-size: 40px;
    letter-spacing: 1.5px;
    text-transform: uppercase;
  }
  .contact {
    position: absolute;
    left: 40px;
    top: 220px;
    font-size: 18px;
    line-height: 1.3;
  }
  .address {
    position: absolute;
    right: 42px;
    bottom: 40px;
    text-align: right;
    font-size: 19px;
    line-height: 1.35;
    font-style: normal;
  }
</style>
</head>
<body>
  <main class="canvas">
    <section class="card card-back" aria-label="Card back">
      <h1 class="company-name">Wiring By Candor, LLC</h1>
    </section>
    <section class="card card-front" aria-label="Card front">
      <h2 class="person-name">Neil Radcott</h2>
      <div class="contact">
        <p class="contact-phone">240-555-0182</p>
        <p class="contact-email">Neilr@wiringbycandorco.example</p>
      </div>
      <address class="address">
        Fernbrooke,<br>MD 20990
      </address>
    </section>
  </main>
</body>
</html>
```